KT Hollin's Brochure - Panelform Systems

Hello,
We have an example of very simple brochure (attached below). We would like you to make it better. More sophisticated. More professional looking. All of the info in the document needs to go in the brochure.
Please let me know if you can execute. I will be happy to send over photos, logos etc, once I know.

```html
<!DOCTYPE html>
<html lang="en">
<head>
<meta charset="utf-8">
<title>KT Hollin's Brochure - Panelform Systems</title>
<link href="https://fonts.googleapis.com/css2?family=Poppins:wght@400;500;600;700;800&display=swap" rel="stylesheet">
<style>
:root{
  --red:#e3202e;
  --navy:#2b3486;
  --grey-dark:#4b4b4d;
  --grey-mid:#9a9ca3;
  --grey-light:#e9eaed;
  --text:#3a3a3c;
  --white:#fff;
}
*{box-sizing:border-box;margin:0;padding:0}
html,body{width:1200px;height:3000px;overflow:hidden;background:#fff;font-family:"Poppins",sans-serif;color:var(--text)}
.canvas{position:relative;width:1200px;height:3000px}
.abs{position:absolute}
.photo{position:absolute}
.shadow{box-shadow:0 4px 14px rgba(0,0,0,.22)}

/* cover */
.cover{position:absolute;left:298px;top:138px;width:598px;height:770px;background:#fff;overflow:hidden}
.cover-top{position:absolute;left:0;top:0;width:598px;height:293px;background:linear-gradient(#f4f4f5,#e6e7e9)}
.brand-name{position:absolute;left:0;width:598px;top:52px;text-align:center;font-weight:700;font-size:40px;letter-spacing:2px;color:var(--navy)}
.brand-tag{position:absolute;left:0;width:598px;top:104px;text-align:center;font-size:10px;letter-spacing:1px;color:var(--navy)}
.cover-headline{position:absolute;left:0;width:598px;top:196px;text-align:center;font-weight:800;font-size:35px;color:#3b3b3d;letter-spacing:-.5px}
.cover-headline em{font-style:normal;color:var(--red)}
.cover-since{position:absolute;left:0;width:598px;top:236px;text-align:center;font-weight:500;font-size:26px;color:var(--grey-mid)}
.cover-since::before,.cover-since::after{content:"";position:absolute;top:17px;width:152px;height:2px;background:#b8b9bd}
.cover-since::before{left:50px}.cover-since::after{right:50px}

/* shared contact */
.contact{position:absolute;left:0;right:0;display:flex;justify-content:center;gap:12px}
.contact span{display:inline-flex;align-items:center;gap:4px;background:var(--navy);border:1px solid #fff;color:#fff;font-weight:500;padding:0 4px;line-height:1.25}
.contact svg{fill:#fff}
.url{position:absolute;left:0;right:0;text-align:center;color:#fff;font-weight:600;letter-spacing:2px}

/* pages */
.page{position:absolute;width:455px;height:587px;background:#fff;overflow:hidden;box-shadow:0 4px 14px rgba(0,0,0,.25)}
.page-title{position:absolute;left:25px;top:22px;font-size:22px;line-height:22px;font-weight:500;color:var(--navy);text-transform:uppercase}
.page-title b{font-weight:800}
.page-foot{position:absolute;left:0;bottom:0;width:455px;height:63px}
.page-foot .contact{top:10px;font-size:11px}
.page-foot .url{top:30px;font-size:19px}
.page-label,.page-num{position:absolute;bottom:6px;font-size:12px;font-weight:700;color:#222}
.page-label{left:30px}.page-num{right:30px}

.ticks{list-style:none;position:absolute}
.ticks li{position:relative;padding-left:15px;font-size:9px;line-height:1.25;padding-bottom:4px;margin-bottom:4px;border-bottom:1px solid #e2e3e6}
.ticks li::before{content:"✓";position:absolute;left:0;top:1px;width:8px;height:8px;border:1px solid var(--red);color:var(--red);font-size:7px;line-height:7px;text-align:center;font-weight:700}
.ticks.big li{font-size:11px}
.ticks.big li::before{top:3px}
.ticks.compact li{padding-bottom:2px;margin-bottom:2px}
.ticks.compact li:last-child{border-bottom:0}

.intro-box{position:absolute;background:var(--grey-light);color:var(--grey-dark);font-size:9px;line-height:1.25;padding:12px 14px 8px 28px}
.intro-box::before{content:"";position:absolute;left:14px;top:12px;width:2px;height:38px;background:var(--red)}
.dark-box{position:absolute;background:var(--grey-dark);color:#fff;font-size:9px;font-weight:600;line-height:1.2;padding:10px 10px 6px 26px}
.dark-box::before{content:"";position:absolute;left:14px;top:10px;width:2px;height:36px;background:var(--red)}
.caption{position:absolute;color:#fff;font-size:10.5px;font-weight:600;text-align:center;display:flex;align-items:center;justify-content:center}
.red{background:var(--red)}.navy{background:var(--navy)}

.feature{position:absolute;left:23px;top:98px;width:405px;height:138px;border:2px solid #d3d4d8;background:#f4f4f6;padding:6px 8px}
.feature-row{display:flex;align-items:center;height:28px;margin-bottom:3px}
.feature-icon{width:30px;height:26px;display:flex;align-items:center;justify-content:center;margin-right:6px}
.feature-text{flex:1;height:26px;color:#fff;font-size:9px;font-weight:600;display:flex;align-items:center;padding-left:8px}

.qc-item{position:absolute;left:23px;width:189px;height:46px;font-size:12px;font-weight:600;line-height:1.15;padding:8px 8px 0 20px}
.qc-item::before{content:"";position:absolute;left:10px;top:9px;width:2px;height:28px;background:var(--red)}
.qc-item.light{background:var(--grey-light);color:#222}
.qc-item.dark{background:var(--grey-dark);color:#fff}
</style>
</head>
<body>
<div class="canvas">

<!-- cover -->
<section class="cover shadow">
  <div class="cover-top"></div>
  <div class="brand-name">KT HOLLIN'S</div>
  <div class="brand-tag">HELPING YOU SEE THE LIGHT</div>
  <h1 class="cover-headline">HELPING YOU SEE THE <em>LIGHT</em></h1>
  <div class="cover-since">SINCE 1994</div>
  <div class="photo" role="img" aria-label="Angular glass curtain wall office building under blue sky with trees" style="left:0;top:293px;width:598px;height:388px;background:linear-gradient(#6f9bd0 0%,#a9c3e2 40%,#5d6d7e 65%,#6f8a4f 90%,#b7b4ac 100%)"></div>
  <svg class="abs" style="left:0;top:681px" width="598" height="89"><polygon points="0,0 598,0 598,50 505,50 478,89 120,89 93,50 0,50" fill="var(--red)"/></svg>
  <div class="contact" style="top:693px;font-size:14px">
    <span><svg width="12" height="12" viewBox="0 0 24 24"><path d="M6.6 10.8a15 15 0 0 0 6.6 6.6l2.2-2.2a1 1 0 0 1 1-.25 11.4 11.4 0 0 0 3.6.57 1 1 0 0 1 1 1V20a1 1 0 0 1-1 1A17 17 0 0 1 3 4a1 1 0 0 1 1-1h3.5a1 1 0 0 1 1 1c0 1.25.2 2.45.57 3.57a1 1 0 0 1-.25 1z"/></svg>555-210-4471</span>
    <span><svg width="12" height="12" viewBox="0 0 24 24"><path d="M6 2h9v6H6zM3 9h18v11H3zm3 3v2h6v-2zm0 4v2h6v-2z"/></svg>555-210-4480</span>
  </div>
  <div class="url" style="top:718px;font-size:25px">www.kthollininc.com</div>
</section>

<!-- page 01 -->
<section class="page" style="left:135px;top:995px">
  <h2 class="page-title">Panelform<br><b>Systems</b></h2>
  <div class="photo" role="img" aria-label="Installers setting a glass unit on a building floor" style="left:180px;top:2px;width:252px;height:157px;background:linear-gradient(135deg,#3f6aa3,#8fb0d4 55%,#4d5560)"></div>
  <div class="abs navy" style="left:432px;top:2px;width:23px;height:157px"></div>
  <ul class="ticks big compact" style="left:25px;top:74px;width:148px">
    <li>Curtain Wall</li><li>Window Wall</li><li>Ribbon Window</li><li>Storefront</li>
  </ul>
  <div class="abs red" style="left:0;top:167px;width:25px;height:205px"></div>
  <div class="photo" role="img" aria-label="Glass office tower above a historic brick building" style="left:25px;top:167px;width:407px;height:205px;background:linear-gradient(#7fa6d4,#4f6f99 60%,#7b4a3c)"></div>
  <div class="abs" style="left:0;top:392px;width:207px;height:117px;background:var(--grey-light);padding:8px 8px 0 25px;font-size:11.5px;font-weight:600;line-height:1.15;color:#222">
    <span style="color:var(--navy);font-weight:800">UNITIZED PRODUCTS</span><br>CAN BE INSTALLED IN ONE THIRD OF THE TIME WITH ONE THIRD OF THE INSTALLERS VERSUS TRADITIONAL STICK PRODUCTS.
  </div>
  <div class="abs" style="left:207px;top:392px;width:3px;height:117px;background:var(--navy)"></div>
  <ul class="ticks" style="left:222px;top:397px;width:210px">
    <li>Enclose a building faster allowing other trades to start earlier.</li>
    <li>Less installers required</li>
    <li>Manufacturing done in a controlled environment</li>
    <li>Standard work and quality control inspections.</li>
  </ul>
  <footer class="page-foot">
    <svg class="abs" width="455" height="63"><polygon points="0,0 455,0 455,30 375,30 355,63 100,63 80,30 0,30" fill="var(--red)"/></svg>
    <div class="contact"><span>☎ 555-210-4471</span><span>▤ 555-210-4480</span></div>
    <div class="url">www.kthollininc.com</div>
    <span class="page-label">PAGE</span><span class="page-num">01</span>
  </footer>
</section>

<!-- page 02 -->
<section class="page" style="left:618px;top:995px">
  <h2 class="page-title">Unitized<br><b>Curtain Wall</b></h2>
  <div class="intro-box" style="left:212px;top:2px;width:216px;height:81px">Designed by installers for installers with quality and efficient installation. Complete up to 40 panels a day with one installation team.</div>
  <div class="abs navy" style="left:428px;top:2px;width:27px;height:81px"></div>
  <div class="feature">
    <div class="feature-row"><div class="feature-icon red"><svg width="14" height="12"><rect x="1" y="1" width="12" height="10" fill="none" stroke="#fff" stroke-width="1.5"/></svg></div><div class="feature-text red">Industry leading 2 1/2" overall adjustment for out of tolerance structures.</div></div>
    <div class="feature-row"><div class="feature-icon navy"><svg width="14" height="12"><path d="M1 3h12M1 6h8M1 9h12" stroke="#fff" stroke-width="1.5"/></svg></div><div class="feature-text navy">Alignment pins allow for 1/4" forgiveness to engage units.</div></div>
    <div class="feature-row"><div class="feature-icon red"><svg width="14" height="12"><rect x="1" y="1" width="6" height="6" fill="#fff"/><rect x="7" y="5" width="6" height="6" fill="none" stroke="#fff" stroke-width="1.5"/></svg></div><div class="feature-text red">Trim clips and anchorsare attached.</div></div>
    <div class="feature-row"><div class="feature-icon navy"><svg width="14" height="12"><rect x="1" y="1" width="12" height="10" fill="none" stroke="#fff" stroke-width="1.5"/><path d="M3 4h8M3 7h8" stroke="#fff"/></svg></div><div class="feature-text navy">Shipped on metal racks or wood crates.</div></div>
  </div>
  <div class="photo" role="img" aria-label="Low-rise glass office campus with landscaping" style="left:23px;top:256px;width:198px;height:210px;background:linear-gradient(#8fb5de,#5a7ea8 55%,#567a45)"></div>
  <div class="caption red" style="left:23px;top:466px;width:198px;height:29px">Meridian Bank Plano Texas</div>
  <div class="photo" role="img" aria-label="Curved glass office tower" style="left:230px;top:256px;width:201px;height:210px;background:linear-gradient(#b9cde4,#6f8fb3 60%,#8d969e)"></div>
  <div class="caption navy" style="left:230px;top:466px;width:201px;height:29px">Parkline 12 Austin Texas</div>
  <footer class="page-foot">
    <svg class="abs" width="455" height="63"><polygon points="0,0 455,0 455,30 375,30 355,63 100,63 80,30 0,30" fill="var(--red)"/></svg>
    <div class="contact"><span>☎ 555-210-4471</span><span>▤ 555-210-4480</span></div>
    <div class="url">www.kthollininc.com</div>
    <span class="page-label">PAGE</span><span class="page-num">02</span>
  </footer>
</section>

<!-- page 03 -->
<section class="page" style="left:135px;top:1618px">
  <h2 class="page-title">Unitized <b>Ribbon Wall &amp;<br>Storefront</b></h2>
  <div class="abs navy" style="left:0;top:75px;width:25px;height:211px"></div>
  <div class="dark-box" style="left:25px;top:75px;width:217px;height:55px">Designed for quality and fast installation. This 2" by 4 1/2" system offers the following benefits:</div>
  <ul class="ticks" style="left:40px;top:142px;width:195px">
    <li>Installed from the interior or exterior</li><li>12 psi water rating</li><li>Higher thermal</li><li>Performance due to thermal strut</li><li>Two color option(interior/exterior)</li><li>Larger panes of glass to improve views</li><li>Shipped on metal racks or wood crates</li>
  </ul>
  <div class="photo" role="img" aria-label="Multi-storey clinic with ribbon windows" style="left:242px;top:75px;width:211px;height:193px;background:linear-gradient(#5d8fd0,#9fbde2 45%,#55606e)"></div>
  <div class="caption red" style="left:242px;top:268px;width:211px;height:18px">Valley Health North</div>
  <div class="abs" style="left:23px;top:297px;width:408px;height:208px;background:#c9cbd0"></div>
  <div class="photo" role="img" aria-label="Long low healthcare building with glass storefront" style="left:29px;top:303px;width:396px;height:176px;background:linear-gradient(#9fb6cf,#d9e1ea 45%,#8d949d 70%,#a89f84)"></div>
  <svg class="abs" style="left:200px;top:297px" width="30" height="22"><polygon points="0,0 30,0 15,22" fill="#fff"/></svg>
  <div class="caption navy" style="left:29px;top:479px;width:396px;height:22px">Valley Health North</div>
  <footer class="page-foot">
    <svg class="abs" width="455" height="63"><polygon points="0,0 455,0 455,30 375,30 355,63 100,63 80,30 0,30" fill="var(--red)"/></svg>
    <div class="contact"><span>☎ 555-210-4471</span><span>▤ 555-210-4480</span></div>
    <div class="url">www.kthollininc.com</div>
    <span class="page-label">PAGE</span><span class="page-num">03</span>
  </footer>
</section>

<!-- page 04 -->
<section class="page" style="left:618px;top:1618px">
  <h2 class="page-title">Unitized<br><b>Window Wall</b></h2>
  <div class="dark-box" style="left:25px;top:75px;width:217px;height:61px">Designed by installers for an efficient installation with large vision areas. This 6" deep window system offers the following benefits:</div>
  <ul class="ticks" style="left:40px;top:148px;width:195px">
    <li>Punched openings or window wall runs</li><li>Installed from the interior using a receptor system</li><li>Metal slab covers</li><li>Trim clips are attached</li><li>Shipped on metal racks or wood crates</li>
  </ul>
  <div class="photo" role="img" aria-label="Brick and glass residential high-rise at a street corner" style="left:242px;top:75px;width:213px;height:170px;background:linear-gradient(#7ea8da,#8a5a4a 55%,#6e6e70)"></div>
  <div class="caption red" style="left:242px;top:245px;width:213px;height:19px">Elm &amp; 4th Denver CO</div>
  <div class="photo" role="img" aria-label="Residential tower with window wall" style="left:23px;top:274px;width:198px;height:213px;background:linear-gradient(#c4d6ea,#8e96a3 50%,#7a6b60)"></div>
  <div class="caption red" style="left:23px;top:487px;width:198px;height:25px">Meridian Bank Plano Texas</div>
  <div class="photo" role="img" aria-label="Building entrance with tall glass storefront" style="left:230px;top:274px;width:201px;height:213px;background:linear-gradient(#b18570,#8fb2c8 50%,#4b4f55)"></div>
  <div class="caption navy" style="left:230px;top:487px;width:201px;height:25px">Parkline 12 Austin Texas</div>
  <footer class="page-foot">
    <svg class="abs" width="455" height="63"><polygon points="0,0 455,0 455,30 375,30 355,63 100,63 80,30 0,30" fill="var(--red)"/></svg>
    <div class="contact"><span>☎ 555-210-4471</span><span>▤ 555-210-4480</span></div>
    <div class="url">www.kthollininc.com</div>
    <span class="page-label">PAGE</span><span class="page-num">04</span>
  </footer>
</section>

<!-- page 05 -->
<section class="page" style="left:135px;top:2238px">
  <h2 class="page-title" style="top:28px">Quality <b>Control</b></h2>
  <svg class="abs" style="left:0;top:54px" width="455" height="26"><polygon points="0,0 262,0 280,17 455,17 455,26 0,26" fill="var(--navy)"/></svg>
  <div class="abs navy" style="left:0;top:78px;width:220px;height:144px"></div>
  <div class="abs navy" style="left:440px;top:78px;width:15px;height:392px"></div>
  <div class="abs" style="left:23px;top:91px;width:189px;height:131px;background:#fff;text-align:center">
    <div style="font-size:62px;font-weight:700;color:var(--red);line-height:70px;letter-spacing:-2px">100%</div>
    <svg class="abs" style="left:0;top:70px" width="189" height="30"><polygon points="0,0 170,0 150,30 0,30" fill="var(--navy)"/></svg>
    <div class="abs" style="left:0;top:72px;width:150px;font-size:21px;font-weight:800;color:#fff">FACTORY</div>
    <div class="abs" style="left:0;top:104px;width:189px;font-size:13px;letter-spacing:6px;font-weight:600;color:#333">ASSEMBLED</div>
  </div>
  <div class="photo" role="img" aria-label="Tall steel test rig holding a glass wall unit inside a factory" style="left:225px;top:91px;width:215px;height:379px;background:linear-gradient(#8a8f98,#4a5a74 50%,#6d6a66)"></div>
  <div class="caption red" style="left:225px;top:470px;width:230px;height:35px">Air and Water Test Chamber</div>
  <div class="qc-item light" style="top:240px">Temperature Controlled Clean Environment</div>
  <div class="qc-item dark" style="top:294px">Lean Standard Work Training and Certification</div>
  <div class="qc-item light" style="top:348px">Sealant Manufacture Certification</div>
  <div class="qc-item dark" style="top:402px">Rigorous Quality Inspections</div>
  <div class="qc-item light" style="top:456px">5% of Completed Units Tested for Air &amp; Water</div>
  <footer class="page-foot">
    <svg class="abs" width="455" height="63"><polygon points="0,0 455,0 455,30 375,30 355,63 100,63 80,30 0,30" fill="var(--red)"/></svg>
    <div class="contact"><span>☎ 555-210-4471</span><span>▤ 555-210-4480</span></div>
    <div class="url">www.kthollininc.com</div>
    <span class="page-label">PAGE</span><span class="page-num">05</span>
  </footer>
</section>

<!-- page 06 -->
<section class="page" style="left:618px;top:2238px">
  <h2 class="page-title" style="top:26px">Design<br><b>Assist</b></h2>
  <div class="intro-box" style="left:125px;top:5px;width:303px;height:69px">Through our Charrette Process, we work together with the entire team to identify the Owner's needs, the Architect's design intent, and the Contractor's schedule and budget.</div>
  <div class="abs navy" style="left:428px;top:5px;width:27px;height:69px"></div>
  <div class="abs red" style="left:0;top:83px;width:23px;height:204px"></div>
  <div class="photo" role="img" aria-label="Design team meeting around a table with laptops and a whiteboard" style="left:23px;top:83px;width:407px;height:204px;background:linear-gradient(#d9dde3,#2f4f93 55%,#5a5f6a)"></div>
  <div class="abs" style="left:0;top:318px;width:190px;height:57px;background:var(--grey-dark);color:#fff;font-size:19px;font-weight:700;line-height:19px;padding:10px 0 0 24px">RESOURCES<br><span style="font-weight:500">WE PROVIDE</span></div>
  <ul class="ticks big compact" style="left:222px;top:296px;width:208px">
    <li>Curtain Wall Designer</li><li>Architect</li><li>Structural Engineer</li><li>Estimator</li><li>Project Manager</li>
  </ul>
  <div class="abs" style="left:23px;top:420px;width:407px;height:96px;border:2px solid var(--navy);background:#f4f4f6"></div>
  <svg class="abs" style="left:23px;top:406px" width="120" height="22"><polygon points="0,0 100,0 115,22 0,22" fill="var(--navy)"/></svg>
  <div class="abs" style="left:33px;top:408px;font-size:11px;font-weight:600;color:#fff">Tools We Use</div>
  <ul class="ticks big compact" style="left:40px;top:434px;width:165px">
    <li>Modelbay for BIM Models</li><li>Mind Map</li><li>Document Tracking</li><li>Product Samples</li>
  </ul>
  <div class="abs" style="left:210px;top:436px;width:2px;height:70px;background:#c4c6cc"></div>
  <ul class="ticks big compact" style="left:222px;top:434px;width:165px">
    <li>Decision Matrix</li><li>Elevation Map</li><li>Budget Updates</li>
  </ul>
  <footer class="page-foot">
    <svg class="abs" width="455" height="63"><polygon points="0,0 455,0 455,30 375,30 355,63 100,63 80,30 0,30" fill="var(--red)"/></svg>
    <div class="contact"><span>☎ 555-210-4471</span><span>▤ 555-210-4480</span></div>
    <div class="url">www.kthollininc.com</div>
    <span class="page-label">PAGE</span><span class="page-num">06</span>
  </footer>
</section>

</div>
</body>
</html>
```